Veltrona Services

Double sided business cards with color on front and black and white on back. I have basic ideas and graphics, but am looking for someone to take them to the next level

```html
<!DOCTYPE html>
<html lang="en">
<head>
<meta charset="utf-8">
<title>Veltrona Services – Business Card</title>
<link rel="stylesheet" href="https://fonts.googleapis.com/css2?family=Barlow+Semi+Condensed:wght@500&display=swap">
<style>
  :root {
    --backdrop: #262626;
    --card-black: #050505;
    --paper: #f7f7f7;
    --paper-shade: #d9d9d9;
    --ink: #0a0a0a;
    --brand-blue: #4a86b0;
    --accent-red: #e0262b;
    --accent-green: #5cbf2a;
    --accent-yellow: #e8c51c;
    --line-white: #f2f2f2;
  }
  html, body {
    margin: 0;
    padding: 0;
    width: 1200px;
    height: 732px;
    overflow: hidden;
    background: var(--backdrop);
  }
  .canvas {
    position: relative;
    width: 1200px;
    height: 732px;
  }
  .card {
    position: absolute;
    top: 242px;
    width: 436px;
    height: 248px;
    background: var(--card-black);
  }
  .card--front { left: 143px; }
  .card--back  { left: 620px; }
  .card svg { display: block; }
  .card-text {
    font-family: "Barlow Semi Condensed", "Arial Narrow", sans-serif;
    font-weight: 500;
    font-size: 23px;
  }
  .company-name { fill: var(--brand-blue); }
  .phone, .tagline { fill: var(--ink); }
  .mark-name { font-size: 22px; }
  .mark-name--front { fill: var(--brand-blue); }
  .mark-name--back { fill: var(--ink); }
</style>
</head>
<body>
<main class="canvas">

  <!-- Front side -->
  <section class="card card--front" aria-label="Business card front">
    <svg width="436" height="248" viewBox="0 0 436 248">
      <defs>
        <linearGradient id="front-paper" x1="0" y1="0" x2="0.3" y2="1">
          <stop offset="0" stop-color="var(--paper)"/>
          <stop offset="0.6" stop-color="#f1f1f1"/>
          <stop offset="1" stop-color="var(--paper-shade)"/>
        </linearGradient>
      </defs>
      <polygon class="paper-panel" points="314,0 436,0 436,209 415,228 86,228" fill="url(#front-paper)"/>
      <polygon class="paper-facet" points="150,110 230,110 160,228 86,228" fill="#000" opacity="0.04"/>
      <line class="accent-red" x1="300" y1="0" x2="138" y2="163" stroke="var(--accent-red)" stroke-width="1"/>
      <line class="accent-green" x1="76" y1="239" x2="291" y2="239" stroke="var(--accent-green)" stroke-width="1"/>
      <line class="accent-yellow" x1="424" y1="236" x2="436" y2="224" stroke="var(--accent-yellow)" stroke-width="1.2"/>

      <g class="brand-mark">
        <circle cx="300" cy="86" r="11" fill="var(--brand-blue)"/>
        <text class="card-text mark-name mark-name--front" x="318" y="94">Veltrona</text>
      </g>

      <text class="card-text company-name" x="412" y="187" text-anchor="end">VELTRONA SERVICES</text>
      <text class="card-text phone" x="412" y="211" text-anchor="end">555-014-2387</text>
    </svg>
  </section>

  <!-- Back side -->
  <section class="card card--back" aria-label="Business card back">
    <svg width="436" height="248" viewBox="0 0 436 248">
      <defs>
        <linearGradient id="back-paper" x1="0.2" y1="0" x2="0.8" y2="1">
          <stop offset="0" stop-color="var(--paper)"/>
          <stop offset="0.6" stop-color="#f0f0f0"/>
          <stop offset="1" stop-color="var(--paper-shade)"/>
        </linearGradient>
      </defs>
      <polygon class="paper-panel" points="0,0 122,0 349,228 21,228 0,209" fill="url(#back-paper)"/>
      <polygon class="paper-facet" points="200,110 270,110 340,228 270,228" fill="#000" opacity="0.04"/>
      <line class="accent-white" x1="134" y1="0" x2="297" y2="163" stroke="var(--line-white)" stroke-width="1"/>
      <line class="accent-white" x1="144" y1="239" x2="359" y2="239" stroke="var(--line-white)" stroke-width="1"/>
      <line class="accent-white" x1="1" y1="214" x2="12" y2="236" stroke="var(--line-white)" stroke-width="1"/>

      <g class="brand-mark">
        <circle cx="30" cy="86" r="11" fill="var(--ink)"/>
        <text class="card-text mark-name mark-name--back" x="48" y="94">Veltrona</text>
      </g>

      <text class="card-text tagline" x="15" y="187">A CURATED EXPERIENCE</text>
      <text class="card-text tagline" x="15" y="211">ALL THAT IS PROMISED IS CLARITY</text>
    </svg>
  </section>

</main>
</body>
</html>
```